Flyer-Design für Onlineshop für Schwimmbäder
Zielgruppe
Onlineshop für Schwimmbäder
Zielgruppe alle Poolbesitzer.
Wichtig ist der Fokus auf die Marke Trelvo-Mint-Shop und Varnelix (jeweils Poolchemie) sowie die Marke Quendor (ebenfalls Poolchemie). Daneben noch den Fokus auf Poolzubehör wie Poolroboter, Stahlwandpools, Poolfolien, Sandfilteranlagen und Pumpen legen.
Aufgabenstellung
Wickelfalzflyer 6 seitig
105 x 210 DIN Lang Hochformat
Ich habe meinen alten Flyer mit Anhang. Bilder können Sie u.a. aus www.trelvo-mint-shop.example holen

```html
<!DOCTYPE html>
<html lang="de">
<head>
<meta charset="utf-8">
<title>Trelvo-Mint-Shop – Wickelfalzflyer</title>
<link href="https://fonts.googleapis.com/css2?family=Bebas+Neue&family=Oswald:wght@600&family=Roboto:wght@500&display=swap" rel="stylesheet">
<style>
  :root {
    --bg: #e6e7e9;
    --paper: #ffffff;
    --navy: #0b3a9c;
    --royal: #1560cc;
    --cyan: #14aee8;
    --sky: #3fc4f0;
    --label: #2b79d2;
    --ink: #0d4aa8;
  }
  * { margin: 0; padding: 0; box-sizing: border-box; }
  html, body { width: 1200px; height: 1200px; overflow: hidden; background: var(--bg); }
  .flyer {
    position: absolute; left: 67px; top: 206px; width: 1066px; height: 790px;
    background: var(--paper); overflow: hidden;
  }
  .waves { position: absolute; inset: 0; width: 100%; height: 100%; }
  .fold { position: absolute; top: 0; bottom: 0; width: 40px; }
  .fold--left { left: 313px; background: linear-gradient(90deg, rgba(0,0,0,0) 0%, rgba(0,0,0,.06) 100%); }
  .fold--right { left: 708px; background: linear-gradient(90deg, rgba(0,0,0,.05) 0%, rgba(0,0,0,0) 100%); }
  .heading {
    position: absolute; width: 304px; text-align: center; line-height: 1;
    font-family: "Bebas Neue", sans-serif; font-weight: 400; font-size: 31px; color: var(--ink); letter-spacing: .5px;
    white-space: nowrap;
  }
  .card { position: absolute; width: 304px; height: 185px; }
  .card__photo { height: 150px; }
  .card__bar {
    height: 35px; background: var(--label); color: #eef5ff; position: relative;
    font-family: "Roboto", sans-serif; font-weight: 500; font-size: 15px; letter-spacing: .6px;
    display: flex; align-items: center; justify-content: center; white-space: nowrap;
  }
  .card__arrow { position: absolute; right: 8px; top: 11px; }
  .brand {
    position: absolute; width: 320px; text-align: center; line-height: 1; white-space: nowrap;
    font-family: "Oswald", sans-serif; font-weight: 600; font-size: 30px; color: var(--ink);
  }
  .url {
    position: absolute; width: 320px; text-align: center; line-height: 1; white-space: nowrap;
    font-family: "Bebas Neue", sans-serif; font-size: 27px; letter-spacing: .2px;
  }
  .url--dark { color: var(--ink); }
  .url--light { color: #ffffff; }
</style>
</head>
<body>
<main class="flyer">
  <svg class="waves" viewBox="0 0 1066 790" preserveAspectRatio="none" aria-hidden="true">
    <path d="M0,0 H800 C600,80 300,120 0,262 Z" fill="var(--cyan)"/>
    <path d="M0,0 H730 C520,70 260,100 0,215 Z" fill="var(--royal)"/>
    <path d="M0,0 H620 C420,45 200,70 0,150 Z" fill="var(--navy)"/>
    <path d="M0,0 H420 C260,25 120,40 0,80 Z" fill="#0a2f86"/>
    <path d="M1066,612 C800,650 500,700 255,790 H1066 Z" fill="var(--sky)"/>
    <path d="M1066,632 C820,680 560,730 350,790 H1066 Z" fill="var(--cyan)"/>
    <path d="M1066,665 C860,710 700,750 560,790 H1066 Z" fill="var(--royal)"/>
    <path d="M1066,715 C930,745 830,770 760,790 H1066 Z" fill="var(--navy)"/>
  </svg>
  <div class="fold fold--left"></div>
  <div class="fold fold--right"></div>

  <!-- Left panel -->
  <h2 class="heading" style="left:20px; top:212px;">TEXTTEXTTEXT</h2>
  <div class="card" style="left:30px; top:248px;">
    <div class="card__photo" role="img" aria-label="Poolzubehör: Schlauch, Kescher, Dosierschwimmer und Testset auf Holzdeck" style="background:linear-gradient(160deg,#5fc6e6 0%,#2a62c8 45%,#b77a48 100%);"></div>
    <div class="card__bar">POOLZUBEHÖR<svg class="card__arrow" width="20" height="12" viewBox="0 0 20 12"><path d="M1 6H18M13 1L18 6L13 11" stroke="#fff" stroke-width="1.6" fill="none"/></svg></div>
  </div>
  <div class="card" style="left:30px; top:456px;">
    <div class="card__photo" role="img" aria-label="Verschiedene Poolpumpen vor einem Pool" style="background:linear-gradient(180deg,#8fb08a 0%,#3e4a4e 45%,#2e8fd0 65%,#d8cfc4 100%);"></div>
    <div class="card__bar">POOLPUMPEN<svg class="card__arrow" width="20" height="12" viewBox="0 0 20 12"><path d="M1 6H18M13 1L18 6L13 11" stroke="#fff" stroke-width="1.6" fill="none"/></svg></div>
  </div>
  <div class="brand" style="left:22px; top:694px;">Trelvo-Mint-Shop</div>
  <div class="url url--dark" style="left:22px; top:736px;">WWW.TRELVO-MINT-SHOP.EXAMPLE</div>

  <!-- Middle panel -->
  <h2 class="heading" style="left:376px; top:166px;">TEXTTEXTTEXT</h2>
  <div class="card" style="left:376px; top:202px;">
    <div class="card__photo" role="img" aria-label="Sandfilteranlagen mit blauen Kesseln auf Holzsteg am Strand" style="background:linear-gradient(180deg,#9fd4e6 0%,#2f7fd0 45%,#4a4a4a 75%,#8a7b6e 100%);"></div>
    <div class="card__bar">SANDFILTERANLAGEN<svg class="card__arrow" width="20" height="12" viewBox="0 0 20 12"><path d="M1 6H18M13 1L18 6L13 11" stroke="#fff" stroke-width="1.6" fill="none"/></svg></div>
  </div>
  <div class="card" style="left:376px; top:411px;">
    <div class="card__photo" role="img" aria-label="Unterwasseransicht eines Pools mit Mosaikfolie" style="background:linear-gradient(180deg,#1f7fcf 0%,#37a9e6 55%,#1d6cc4 100%);"></div>
    <div class="card__bar">POOLFOLIEN<svg class="card__arrow" width="20" height="12" viewBox="0 0 20 12"><path d="M1 6H18M13 1L18 6L13 11" stroke="#fff" stroke-width="1.6" fill="none"/></svg></div>
  </div>
  <div class="url url--light" style="left:368px; top:740px;">WWW.TRELVO-MINT-SHOP.EXAMPLE</div>

  <!-- Right panel -->
  <div class="brand" style="left:729px; top:34px;">Trelvo-Mint-Shop</div>
  <h2 class="heading" style="left:730px; top:124px;">TEXTTEXTTEXT</h2>
  <div class="card" style="left:730px; top:160px;">
    <div class="card__photo" role="img" aria-label="Poolroboter am Beckenrand" style="background:linear-gradient(180deg,#2f7dcc 0%,#2a6cb8 50%,#a99a86 75%,#c9b9a4 100%);"></div>
    <div class="card__bar">POOLROBOTER<svg class="card__arrow" width="20" height="12" viewBox="0 0 20 12"><path d="M1 6H18M13 1L18 6L13 11" stroke="#fff" stroke-width="1.6" fill="none"/></svg></div>
  </div>
  <div class="card" style="left:730px; top:369px;">
    <div class="card__photo" role="img" aria-label="Wasserpflegeprodukte in Eimern und Dosen vor Palmen" style="background:linear-gradient(180deg,#8bbf6a 0%,#e8eef4 45%,#3a7fd0 75%,#9a7a5c 100%);"></div>
    <div class="card__bar">VARNELIX WASSERPFLEGE<svg class="card__arrow" width="20" height="12" viewBox="0 0 20 12"><path d="M1 6H18M13 1L18 6L13 11" stroke="#fff" stroke-width="1.6" fill="none"/></svg></div>
  </div>
  <div class="url url--light" style="left:727px; top:736px;">WWW.TRELVO-MINT-SHOP.EXAMPLE</div>
</main>
</body>
</html>
```